Global social media analytics company needs business card design

We need an updated business card design to align with our new website - plumvantix.com -

I would also like a favicon designed as well.

Target Market(s)

CEOs, CMOs go big companies

Industry/Entity Type

Business

Contact Information for Business Card

Room for the following:
Address
Main telephone
Direct telephone or cell phone
twitter handle

Colors
aaaaaa

Requirements
Must have
• Attention to detail; style.
• Use the logo color from our website - which is gray

```html
<!DOCTYPE html>
<html lang="en">
<head>
<meta charset="utf-8">
<title>Plumvantix business cards</title>
<link rel="stylesheet" href="https://fonts.googleapis.com/css2?family=Mulish:wght@300;400;800&display=swap">
<style>
  :root {
    --page: #e0e0e0;
    --card: #ffffff;
    --brand-gray: #3d3d3d;
    --ink: #2b2b2b;
    --muted: #4a4a4a;
    --rule: #b9b9b9;
    --faint: #f1f0ee;
    --white: #ffffff;
  }
  * { margin: 0; padding: 0; box-sizing: border-box; }
  html, body { width: 776px; height: 1200px; overflow: hidden; }
  body {
    position: relative;
    background: var(--page);
    font-family: "Mulish", "Helvetica Neue", Arial, sans-serif;
    color: var(--ink);
  }
  .card {
    position: absolute;
    left: 99px;
    width: 578px;
    height: 330px;
    background: var(--card);
    overflow: hidden;
  }
  .card--front { top: 82px; }
  .card--back { top: 435px; }
  .card--alt { top: 787px; }

  .city-photo {
    position: absolute; inset: 0;
    background:
      linear-gradient(180deg, rgba(0,0,0,0) 62%, rgba(60,45,40,0.55) 100%),
      linear-gradient(90deg, #6f6a66 0%, #b8a48a 22%, #e3d8c6 45%, #e8dcc4 55%, #b49c7e 78%, #726b66 100%);
  }
  .wordmark { position: absolute; display: flex; align-items: center; }
  .wordmark__dot { border-radius: 50%; flex: none; }
  .wordmark__name { font-weight: 800; letter-spacing: -0.02em; line-height: 1; }

  .wordmark--hero { left: 83px; top: 113px; }
  .wordmark--hero .wordmark__dot { width: 106px; height: 106px; background: var(--white); margin-right: 18px; }
  .wordmark--hero .wordmark__name { font-size: 44px; color: var(--white); }

  .wordmark--back { left: 61px; top: 141px; }
  .wordmark--back .wordmark__dot { width: 48px; height: 48px; background: var(--brand-gray); margin-right: 7px; }
  .wordmark--back .wordmark__name { font-size: 20px; color: var(--brand-gray); }

  .wordmark--alt { left: 60px; top: 274px; }
  .wordmark--alt .wordmark__dot { width: 31px; height: 31px; background: var(--brand-gray); margin-right: 5px; }
  .wordmark--alt .wordmark__name { font-size: 14px; color: var(--brand-gray); }

  .backdrop-circle {
    position: absolute; left: -150px; top: 80px;
    width: 355px; height: 355px; border-radius: 50%;
    background: var(--faint);
  }
  .rule { position: absolute; width: 1px; background: var(--rule); }

  .person-name { position: absolute; font-weight: 300; font-size: 18px; color: var(--ink); }
  .person-role { position: absolute; font-size: 10.5px; color: var(--ink); }
  .contact {
    position: absolute; list-style: none;
    font-size: 10.3px; font-weight: 400; color: var(--muted); line-height: 12px;
  }
  .contact li { display: flex; align-items: flex-start; }
  .contact svg { width: 9px; height: 10px; margin-right: 5px; margin-top: 1px; flex: none; fill: var(--muted); }

  .alt-name { position: absolute; left: 0; width: 100%; text-align: center; font-weight: 800; font-size: 21px; top: 138px; color: var(--ink); }
  .alt-role { position: absolute; left: 0; width: 100%; text-align: center; font-weight: 800; font-size: 11px; top: 165px; color: var(--ink); }
</style>
</head>
<body>
  <svg width="0" height="0" style="position:absolute">
    <defs>
      <symbol id="i-pin" viewBox="0 0 10 12"><path d="M5 0a4 4 0 0 1 4 4c0 3-4 8-4 8S1 7 1 4a4 4 0 0 1 4-4zm0 2.3A1.7 1.7 0 1 0 5 5.7 1.7 1.7 0 0 0 5 2.3z"/></symbol>
      <symbol id="i-phone" viewBox="0 0 10 10"><path d="M0 3.5C0 1.5 2 1 5 1s5 .5 5 2.5V4H7.5V3h-5v1H0zM2 5h6l1.5 4.5h-9z"/></symbol>
      <symbol id="i-mobile" viewBox="0 0 10 12"><path d="M2 0h6v12H2zm1 1.5v8h4v-8z"/></symbol>
      <symbol id="i-mail" viewBox="0 0 10 10"><path d="M0 2h10v6H0zm1 1v.4l4 2.4 4-2.4V3z"/></symbol>
      <symbol id="i-globe" viewBox="0 0 10 10"><path d="M5 .5a4.5 4.5 0 1 0 0 9 4.5 4.5 0 0 0 0-9zm0 1c.7 0 1.4 1.5 1.5 3h-3C3.6 3 4.3 1.5 5 1.5zm-1.5 4h3C6.4 7 5.7 8.5 5 8.5S3.6 7 3.5 5.5z"/></symbol>
      <symbol id="i-dot" viewBox="0 0 10 10"><circle cx="5" cy="5" r="4"/></symbol>
    </defs>
  </svg>

  <section class="card card--front">
    <div class="city-photo" role="img" aria-label="Motion-blurred photo of a busy city street with pedestrians crossing between tall buildings"></div>
    <div class="wordmark wordmark--hero">
      <span class="wordmark__dot"></span>
      <span class="wordmark__name">plumvantix</span>
    </div>
  </section>

  <section class="card card--back">
    <div class="backdrop-circle"></div>
    <div class="wordmark wordmark--back">
      <span class="wordmark__dot"></span>
      <span class="wordmark__name">plumvantix</span>
    </div>
    <div class="rule" style="left:290px; top:56px; height:217px;"></div>
    <div class="person-name" style="left:310px; top:73px;">Marcus Hale</div>
    <div class="person-role" style="left:310px; top:96px;">Founder &amp; CEO</div>
    <ul class="contact" style="left:310px; top:126px;">
      <li><svg><use href="#i-pin"/></svg><span>820 Linden Park Ave. 4th Fl<br>Ashford, MA 02190<br>USA</span></li>
    </ul>
    <ul class="contact" style="left:310px; top:173px; line-height:15.5px;">
      <li><svg><use href="#i-phone"/></svg><span>+1 555 014 2290</span></li>
      <li><svg><use href="#i-mobile"/></svg><span>+1 555 014 2290</span></li>
    </ul>
    <ul class="contact" style="left:310px; top:211px; line-height:15px;">
      <li><svg><use href="#i-mail"/></svg><span>marcus@plumvantix.com</span></li>
      <li><svg><use href="#i-globe"/></svg><span>www.plumvantix.com</span></li>
      <li><svg><use href="#i-dot"/></svg><span>@Plumvantix</span></li>
    </ul>
  </section>

  <section class="card card--alt">
    <div class="alt-name">Marcus Hale</div>
    <div class="alt-role">Founder &amp; CEO</div>
    <div class="wordmark wordmark--alt">
      <span class="wordmark__dot"></span>
      <span class="wordmark__name">plumvantix</span>
    </div>
    <div class="rule" style="left:205px; top:270px; height:40px;"></div>
    <ul class="contact" style="left:225px; top:268px; line-height:14.5px;">
      <li><svg><use href="#i-pin"/></svg><span>820 Linden Park Ave. 4th Fl<br>Ashford, MA 02190<br>USA</span></li>
    </ul>
    <div class="rule" style="left:405px; top:270px; height:40px;"></div>
    <ul class="contact" style="left:426px; top:268px; line-height:14.5px;">
      <li><svg><use href="#i-phone"/></svg><span>+1 555 014 2290</span></li>
      <li><svg><use href="#i-mobile"/></svg><span>+1 555 014 2290</span></li>
      <li><svg><use href="#i-dot"/></svg><span>@Plumvantix</span></li>
    </ul>
  </section>
</body>
</html>
```